Webdesign für freiberuflichen Statiker
Zielgruppe
Ich bin seit 2021 freiberuflicher Statiker. Ich arbeite mit anderen Freelancern / Partnern / Firmen zusammen und lasse von ihnen z.B. Pläne zeichnen. Meine aktuelle Website habe ich selbst designed, mit Wordpress. Diese soll nun aber komplett neu gestaltet werden. Meine Domain www.vendrik-statik.de möchte ich möglichst behalten.
Meine Zielgruppe sind Architekturbüros, Bauträger, private und öffentliche Bauherren. Sie sollen vor allem einen visuellen Eindruck von unserer Arbeit bekommen - durch Fotos (und einem Video auf der Startseite) von Baustellen, von unseren 3D-Modellen oder Berechnungsmodellen.
Aufgabenstellung
Es gibt bereits ein neues Logo. Dieses werde ich mit anhängen. Außerdem habe ich eine pdf-Datei vorbereitet ('SBV_Inhalte Website'), die den groben Aufbau der Website vorgibt und der die Texte entnommen werden können. Auf der ersten Seite des Dokuments stehen außerdem 3 Beispiel-Websites, die ich gut finde und an denen Ihr euch orientieren könnt. Die Farbwahl kann sehr schlicht gehalten werden - ähnlich wie bei den 3 Beispiel-Seiten. Ich liefere eigene Bilder mit, für projektunabhängige Inhalte können aber auch andere Bilder verwendet werden.

```html
<!DOCTYPE html>
<html lang="de">
<head>
<meta charset="utf-8">
<title>SBV – Individuelle Tragwerkslösungen</title>
<link href="https://fonts.googleapis.com/css2?family=Montserrat:wght@400;500;600;700&display=swap" rel="stylesheet">
<style>
:root{
  --ink:#111111;
  --text:#333333;
  --muted:#555555;
  --accent:#d9534f;
  --line:#9a9a9a;
  --paper:#ffffff;
  --footer:#000000;
  --hero-a:#c9ccc6;
  --hero-b:#e4e4e1;
  --hero-c:#b6bdaa;
  --render-a:#d9dde3;
  --render-b:#8c8f94;
  --render-c:#a5815f;
  --site-a:#8a8d8c;
  --site-b:#cfd0cc;
  --wood-a:#ead9c6;
  --wood-b:#f5efe6;
}
*{margin:0;padding:0;box-sizing:border-box}
html,body{width:1200px;height:3013px;overflow:hidden;background:var(--paper)}
body{position:relative;font-family:"Montserrat",Arial,sans-serif;color:var(--ink)}
.abs{position:absolute}
.accent-line{position:absolute;height:1px;background:var(--accent)}
.brand{font-weight:700;letter-spacing:1px;color:var(--ink)}
/* hero */
.hero{left:0;top:0;width:1200px;height:750px;background:linear-gradient(160deg,var(--hero-c) 0%,var(--hero-b) 35%,var(--hero-a) 60%,var(--hero-b) 100%)}
.hero .brand{left:124px;top:20px;font-size:44px}
.menu{left:1039px;top:34px;width:37px;height:26px}
.eyebrow{left:205px;top:180px;font-size:19px;font-weight:500;letter-spacing:.5px}
.hero-title{left:123px;top:240px;font-size:72px;font-weight:500;line-height:67px;letter-spacing:1px}
.down-box{left:123px;top:651px;width:55px;height:55px;border:1px solid var(--ink)}
.caption{left:802px;top:650px;color:var(--ink)}
.caption .name{font-size:16px;font-weight:700;display:inline-block;border-bottom:1px solid var(--accent);padding-bottom:2px}
.caption .sub{font-size:16px;margin-top:5px;letter-spacing:.3px}
.caption .small{font-size:10px;margin-top:2px}
/* sections */
.section-title{font-size:38px;font-weight:500;line-height:43px;letter-spacing:.5px;color:var(--ink)}
.more{font-size:16px;color:var(--muted);display:flex;align-items:center;gap:12px}
.card-img{width:299px;height:220px;background:linear-gradient(135deg,var(--render-a) 0%,#eef0f2 40%,var(--render-b) 75%,var(--render-c) 100%)}
.card-label{font-size:19px;font-weight:500;line-height:28px;letter-spacing:.3px}
.card-rule{height:1px;background:var(--line)}
.row{left:123px;width:953px;height:105px;border-top:1px solid var(--line)}
.row .num{position:absolute;left:82px;top:25px;width:55px;height:55px;border:1px solid var(--ink);border-radius:50%;display:flex;align-items:center;justify-content:center;font-size:27px;font-weight:500}
.row .label{position:absolute;left:164px;top:40px;font-size:19px;font-weight:500;letter-spacing:.5px}
.row .thumb{position:absolute;right:0;top:0;width:137px;height:104px;background:linear-gradient(135deg,var(--render-a),var(--render-b) 70%,var(--render-c))}
.project{left:123px;top:2103px;width:953px;height:309px;border:1px solid var(--ink)}
.project .photo{position:absolute;left:0;top:0;width:463px;height:307px;background:linear-gradient(170deg,var(--site-a) 0%,var(--site-b) 45%,var(--site-a) 100%)}
.project .body{position:absolute;left:490px;top:20px;width:440px}
.project h3{font-size:23px;font-weight:500;letter-spacing:.5px}
.meta{display:flex;align-items:center;gap:10px;font-size:19px;margin-top:16px;color:var(--text)}
.project p{font-size:16px;line-height:25px;color:var(--muted);margin-top:28px}
.project .link{font-size:16px;color:var(--muted);margin-top:22px;display:flex;align-items:center;gap:8px}
.cta{left:0;top:2538px;width:1200px;height:318px;background:linear-gradient(120deg,var(--wood-a) 0%,var(--wood-b) 45%,var(--wood-a) 100%)}
.button{left:777px;top:2663px;width:299px;height:54px;border:1px solid var(--ink);display:flex;align-items:center;justify-content:center;gap:12px;font-size:19px;font-weight:500;letter-spacing:.5px}
.footer{left:0;top:2856px;width:1200px;height:157px;background:var(--footer);color:#fff}
.footer .brand{color:#fff;position:absolute;left:126px;top:44px;font-size:40px}
.footer .copy{position:absolute;left:126px;top:121px;font-size:12px}
.footer .legal{position:absolute;right:124px;top:70px;font-size:15px;display:flex;gap:14px}
</style>
</head>
<body>

<header class="abs hero" role="img" aria-label="Luftaufnahme einer Baustelle mit Straße und Kreisverkehr"></header>
<div class="abs brand" style="left:124px;top:18px;font-size:44px">SBV</div>
<svg class="abs menu" viewBox="0 0 37 26" aria-label="Menü"><g stroke="#111" stroke-width="2"><line x1="0" y1="2" x2="37" y2="2"/><line x1="5" y1="13" x2="37" y2="13"/><line x1="0" y1="24" x2="37" y2="24"/></g></svg>
<div class="accent-line" style="left:123px;top:191px;width:55px"></div>
<div class="abs eyebrow">WIR GEHEN NEUE WEGE</div>
<h1 class="abs hero-title">INDIVIDUELLE<br>TRAGWERKSLÖSUNGEN</h1>
<div class="abs down-box"><svg width="53" height="53" viewBox="0 0 53 53"><g fill="none" stroke="#111" stroke-width="2"><line x1="26.5" y1="12" x2="26.5" y2="41"/><polyline points="14,29 26.5,41 39,29"/></g></svg></div>
<div class="abs caption">
  <div class="name">HOTEL VELBERT</div>
  <div class="sub">NEUBAU EINES HOTELGEBÄUDES</div>
  <div class="small">ARCHITEKTEN: HALVORSEN HOTEL CONCEPTS</div>
</div>

<!-- Antrieb -->
<div class="accent-line" style="left:123px;top:863px;width:218px"></div>
<h2 class="abs section-title" style="left:123px;top:884px">WAS UNS BEI JEDEM<br>PROJEKT ANTREIBT</h2>
<div class="abs more" style="left:861px;top:915px">Mehr über unser Office <svg width="22" height="14" viewBox="0 0 22 14"><g fill="none" stroke="#111" stroke-width="1.6"><line x1="0" y1="7" x2="20" y2="7"/><polyline points="14,1 20,7 14,13"/></g></svg></div>

<div class="abs card-img" style="left:123px;top:1014px" role="img" aria-label="Architekturvisualisierung mit Skizzenlinien"></div>
<div class="abs card-img" style="left:450px;top:1014px" role="img" aria-label="Architekturvisualisierung mit Skizzenlinien"></div>
<div class="abs card-img" style="left:777px;top:1014px" role="img" aria-label="Architekturvisualisierung mit Skizzenlinien"></div>
<div class="abs card-label" style="left:123px;top:1254px">WER WIR SIND</div>
<div class="abs card-label" style="left:450px;top:1254px">WIE WIR IHR PROJEKT<br>WEITERBRINGEN</div>
<div class="abs card-label" style="left:777px;top:1254px">WO UNSERE STÄRKEN<br>LIEGEN</div>
<div class="abs card-rule" style="left:123px;top:1330px;width:300px"></div>
<div class="abs card-rule" style="left:450px;top:1330px;width:300px"></div>
<div class="abs card-rule" style="left:777px;top:1330px;width:300px"></div>

<!-- Expertise -->
<div class="accent-line" style="left:123px;top:1449px;width:218px"></div>
<h2 class="abs section-title" style="left:123px;top:1468px">UNSERE EXPERTISE</h2>
<div class="abs more" style="left:922px;top:1479px">Mehr erfahren <svg width="22" height="14" viewBox="0 0 22 14"><g fill="none" stroke="#111" stroke-width="1.6"><line x1="0" y1="7" x2="20" y2="7"/><polyline points="14,1 20,7 14,13"/></g></svg></div>
<div class="abs row" style="top:1556px"><div class="num">01</div><div class="label">STATISCHE BERECHNUNGEN</div><div class="thumb" role="img" aria-label="Architekturvisualisierung"></div></div>
<div class="abs row" style="top:1661px"><div class="num">02</div><div class="label">AUSFÜHRUNGSPLÄNE</div><div class="thumb" role="img" aria-label="Architekturvisualisierung"></div></div>
<div class="abs row" style="top:1766px"><div class="num">03</div><div class="label">THERMISCHE BAUPHYSIK</div><div class="thumb" role="img" aria-label="Architekturvisualisierung"></div></div>
<div class="abs card-rule" style="left:123px;top:1872px;width:953px"></div>

<!-- Arbeit -->
<div class="accent-line" style="left:123px;top:1994px;width:218px"></div>
<h2 class="abs section-title" style="left:123px;top:2014px">AUSZUG UNSERER AKTUELLEN ARBEIT</h2>
<div class="abs more" style="left:941px;top:2026px">Alle Projekte <svg width="22" height="14" viewBox="0 0 22 14"><g fill="none" stroke="#111" stroke-width="1.6"><line x1="0" y1="7" x2="20" y2="7"/><polyline points="14,1 20,7 14,13"/></g></svg></div>
<div class="abs project">
  <div class="photo" role="img" aria-label="Luftaufnahme des eingerüsteten Hotelrohbaus an einer Kreuzung"></div>
  <div class="body">
    <h3>NEUBAU HOTEL ORION</h3>
    <div class="meta"><svg width="20" height="18" viewBox="0 0 20 18"><g fill="none" stroke="#d9534f" stroke-width="1.4"><polygon points="1,5 7,3 13,5 19,3 19,16 13,17 7,15 1,17"/><circle cx="10" cy="8" r="2.5"/></g></svg>VELBERT, DEUTSCHLAND</div>
    <div class="meta"><svg width="18" height="18" viewBox="0 0 18 18"><rect x="1" y="1" width="16" height="16" fill="none" stroke="#d9534f" stroke-width="1.4" stroke-dasharray="3 2"/></svg>CA. 4600 QM</div>
    <p>Lorem ipsum dolor sit amet, consetetur sadipscing elitr, sed diam nonumy eirmod tempor invidunt ut labore et dolore magna aliquyam</p>
    <div class="link">Projekt ansehen <svg width="22" height="14" viewBox="0 0 22 14"><g fill="none" stroke="#111" stroke-width="1.6"><line x1="0" y1="7" x2="20" y2="7"/><polyline points="14,1 20,7 14,13"/></g></svg></div>
  </div>
</div>

<!-- CTA -->
<section class="abs cta" role="img" aria-label="Holztragwerk einer Dachkonstruktion, hell überblendet"></section>
<div class="accent-line" style="left:123px;top:2644px;width:218px"></div>
<h2 class="abs section-title" style="left:123px;top:2665px">WIR SIND IHR ZUVERLÄSSIGER<br>PARTNER</h2>
<div class="abs button">KONTAKT AUFNEHMEN <svg width="24" height="16" viewBox="0 0 24 16"><g fill="none" stroke="#111" stroke-width="1.8"><line x1="0" y1="8" x2="22" y2="8"/><polyline points="15,1 22,8 15,15"/></g></svg></div>

<footer class="abs footer">
  <div class="brand">SBV</div>
  <div class="copy">© 2024 kantwerk-media.com</div>
  <div class="legal"><span>Impressum</span><span>Datenschutz</span></div>
</footer>

</body>
</html>
```